Business Card Design - ThriveMetric

Looking for creative, modern design, two sided for ThriveMetric that is consistent with color and feel of website www.thrivemetric.net.

Back of card will be used to promote products or have a quote revolving around decisions, change, leadership, innovation, creativity. Back should also have space to promote website, but optional to use the icon. Front of the card will need to use the icon and have standard place for name, job title, phone and email. We are not looking to put a mailing address or fax. Also want space to place a few words/phrase explaining what we do...such as individual growth and organizational development or tools, training, information...in addition, want the linkpage icon small on the front somewhere as we are also on linkpage.

Vector file uploaded of icon.

Target Market(s)

Professional coaching for individual growth and organizational development

Industry/Entity Type

Business

Requirements
Must have
• Icon...see attached.

```html
<!DOCTYPE html>
<html lang="en">
<head>
<meta charset="utf-8">
<title>ThriveMetric Business Card</title>
<link rel="stylesheet" href="https://fonts.googleapis.com/css2?family=Arimo:wght@400;700&family=Marcellus&family=Crimson+Text:wght@400&display=swap">
<style>
  :root {
    --page-bg: #eceef2;
    --front-top: #8a8fe0;
    --front-mid: #c9cdf2;
    --front-low: #ffffff;
    --wave-blue: #1f6fd6;
    --wave-light: #a9cdf0;
    --brand-bar: #5566d4;
    --ink: #111111;
    --icon-blue: #1a5fd0;
    --back-cyan: #56d4f2;
    --back-cyan-light: #a8ecfb;
    --back-band: #1d4a66;
    --back-band-light: #dff3fb;
    --footer-black: #0c0c0c;
    --white: #ffffff;
  }
  * { margin: 0; padding: 0; box-sizing: border-box; }
  html, body { width: 922px; height: 1200px; overflow: hidden; background: var(--page-bg); }
  .canvas { position: relative; width: 922px; height: 1200px; }

  .card { position: absolute; left: 108px; width: 706px; height: 471px; overflow: hidden; box-shadow: 0 4px 14px rgba(0,0,0,.18); }
  .card-front { top: 40px; background: linear-gradient(180deg, var(--front-top) 0%, var(--front-mid) 55%, var(--front-low) 100%); }
  .card-back { top: 600px; background: linear-gradient(180deg, var(--back-cyan-light) 0%, var(--back-cyan) 60%); }
  .card svg.waves { position: absolute; left: 0; top: 0; width: 706px; height: 471px; }

  .brand-emblem { position: absolute; left: 46px; top: 30px; width: 246px; height: 246px; border-radius: 50%;
    background: radial-gradient(circle at 50% 50%, #dff0fb 0 45%, #2b7fe0 46% 52%, #cfe3f5 53% 62%, #2c78d8 63% 100%); }
  .accent-swoosh { position: absolute; left: 4px; top: 300px; width: 94px; height: 50px; border-radius: 0 40px 0 40px;
    background: linear-gradient(135deg, #bfe0f7, #3d8fd8); }
  .figure-silhouette { position: absolute; left: 598px; top: 362px; width: 107px; height: 109px; border-radius: 50% 50% 0 0;
    background: #1b1b1b; }

  .brand-bar { position: absolute; left: 382px; top: 223px; width: 324px; height: 34px; background: var(--brand-bar);
    border-radius: 6px 0 0 6px; }
  .brand-name { position: absolute; left: 390px; top: 222px; font: 400 33px/36px "Marcellus", serif; color: var(--white); }
  .contact-fields { position: absolute; left: 384px; top: 272px; font: 400 21px/27px "Arimo", sans-serif; color: var(--ink); }
  .contact-icon { position: absolute; left: 384px; width: 36px; height: 36px; border-radius: 50%;
    background: radial-gradient(circle at 40% 30%, #7fb6ff, var(--icon-blue) 70%); border: 2px solid #cfe0ff; }
  .contact-icon svg { width: 100%; height: 100%; }
  .icon-home { top: 337px; } .icon-phone { top: 382px; } .icon-web { top: 421px; }

  .tagline { position: absolute; left: 44px; top: 352px; width: 305px; font: 400 18px/23.5px "Arimo", sans-serif; color: var(--ink); }
  .social-bar { position: absolute; left: 42px; top: 433px; width: 246px; height: 18px; border-radius: 9px;
    background: var(--brand-bar); display: flex; align-items: center; gap: 8px; padding-left: 6px; }
  .social-dot { width: 12px; height: 12px; background: var(--white); }
  .social-text { font: 400 14px/18px "Arimo", sans-serif; color: var(--white); }

  .back-title { position: absolute; left: 0; width: 100%; top: 126px; text-align: center; font: 400 34px/40px "Marcellus", serif;
    color: var(--ink); text-shadow: 1px 1px 0 rgba(255,255,255,.6); }
  .back-url { position: absolute; left: 0; width: 100%; top: 166px; text-align: center; font: 400 15px/18px "Marcellus", serif;
    color: var(--ink); text-decoration: underline; }
  .quote-list { position: absolute; left: 15px; top: 196px; list-style: none; font: 400 13.5px/17px "Crimson Text", serif; color: var(--ink); }
  .quote-list li { display: flex; align-items: center; gap: 8px; height: 17px; white-space: nowrap; }
  .quote-list li::before { content: "\2192"; font: 700 15px/17px "Arimo", sans-serif; width: 18px; flex: none; }
  .open-book { position: absolute; left: 520px; top: 296px; width: 170px; height: 142px;
    background: linear-gradient(160deg, #ffffff 0%, #bcd7f2 55%, #2f63c9 100%); clip-path: polygon(10% 45%, 70% 10%, 100% 40%, 45% 100%); }
  .value-strip { position: absolute; left: 0; bottom: 0; width: 100%; height: 26px; background: var(--footer-black);
    color: var(--white); font: 400 18px/26px "Crimson Text", serif; padding-left: 26px; }
</style>
</head>
<body>
<main class="canvas">

  <section class="card card-front" aria-label="Card front">
    <svg class="waves" viewBox="0 0 706 471" aria-hidden="true">
      <path d="M0 0 H706 V150 C620 90 520 50 400 30 C280 10 120 20 0 60 Z" fill="var(--wave-light)"/>
      <path d="M0 30 C150 -5 300 5 420 30 C540 55 640 110 706 150 V118 C640 80 540 40 420 18 C300 -4 150 -10 0 14 Z" fill="var(--wave-blue)"/>
    </svg>
    <div class="brand-emblem" role="img" aria-label="Brand icon: profile head with gears inside circular blue arrows"></div>
    <div class="accent-swoosh" role="img" aria-label="Light blue curled ribbon decoration"></div>
    <div class="figure-silhouette" role="img" aria-label="Dark silhouette illustration of a thinking figure"></div>

    <div class="brand-bar"></div>
    <div class="brand-name">ThriveMetric</div>
    <div class="contact-fields"><div>Name-</div><div>Job Title-</div></div>

    <div class="contact-icon icon-home"><svg viewBox="0 0 36 36"><path d="M9 19 L18 10 L27 19 M12 17 V26 H24 V17" fill="none" stroke="#fff" stroke-width="2.5"/></svg></div>
    <div class="contact-icon icon-phone"><svg viewBox="0 0 36 36"><path d="M12 10 C10 14 14 22 22 26 L25 23 L21 20 L19 22 C16 20 15 18 14 16 L16 14 L13 10 Z" fill="#fff"/></svg></div>
    <div class="contact-icon icon-web"><svg viewBox="0 0 36 36"><circle cx="18" cy="18" r="8" fill="none" stroke="#fff" stroke-width="2"/><path d="M10 18 H26 M18 10 C14 14 14 22 18 26 C22 22 22 14 18 10" fill="none" stroke="#fff" stroke-width="1.5"/></svg></div>

    <p class="tagline">Providing tools,training,information and collaboration to achieve the results you want.</p>
    <div class="social-bar"><span class="social-dot"></span><span class="social-text">We are also on linkpage</span></div>
  </section>

  <section class="card card-back" aria-label="Card back">
    <svg class="waves" viewBox="0 0 706 471" aria-hidden="true">
      <path d="M0 0 H706 V60 C560 50 300 60 0 140 Z" fill="var(--back-band-light)"/>
      <path d="M0 140 C300 60 560 40 706 60 V70 C560 52 300 72 0 150 Z" fill="var(--back-band)"/>
    </svg>
    <h1 class="back-title">THRIVEMETRIC</h1>
    <div class="back-url">WWW.THRIVEMETRIC.NET</div>
    <ul class="quote-list">
      <li>"Try not to become a man of success, but rather a man of value."</li>
      <li>"We are what we repeatedly do. Excellence is not an act, it is a habit."</li>
      <li>"Life is not fair - get used to it."</li>
      <li>"The only constant is change."</li>
      <li>"Simplicity is the ultimate sophistication."</li>
      <li>"Every man I meet is my superior in some way."</li>
      <li>"The essential part of creativity is not being afraid to fail."</li>
      <li>"Music gives a soul to the universe, wings to the mind, flight to the imagination and life to everything."</li>
      <li>"I'll make the right decision, whichever one it is. I haveto be 100 percent, not 95 or 99."</li>
      <li>"The height of cultivation runs to simplicity."</li>
      <li>"When you are finished changing, you're finished."</li>
      <li>"You learn when you listen. You earn whenyou listen—not just money, but respect."</li>
      <li>"Seek first to understand, then to be understood."</li>
      <li>"The height of cultivation runs to simplicity."</li>
    </ul>
    <div class="open-book" role="img" aria-label="Illustration of an open book with a pencil"></div>
    <div class="value-strip">Live every day with: Passion &#9679; Wonder &#9679; Playfulness &#9679; Love &#9679; Gratitude</div>
  </section>

</main>
</body>
</html>
```